Web Design Project - Investor Services

I would like a simple and elegant web design for my company "Torvelo Management". The company will provide services to Corporate and Institutional investors for their needs with local/foreign investment vehicles. The website will have four pages to start: home, about us, services, contact.
I already chose a logo, and I will attach the source file. The color that I will most probably use for the logo will be blue, and i also like grey with a white background. For the website I would like to see light colors, maybe light green or grey, with the logo either in blue, grey or white (depeding on the background).
Target Market(s)
Investment managers and tax/legal advisors from top firms. This is the reason why I want something simple and elegant.
Industry/Entity Type
Investment
Requirements
Nice to have
- I do not want many pictures in the website, but I might include a couple of pictures of Madrid and maybe a picture of myself in the about us page (still deciding). I will attach some pictures of Madrid that I like, but feel free to search for others - i have others but i am not able to attach all of them.

```html
<!DOCTYPE html>
<html lang="en">
<head>
<meta charset="utf-8">
<title>Torvelo Management</title>
<link rel="stylesheet" href="https://fonts.googleapis.com/css2?family=PT+Sans:wght@400;700&family=PT+Sans+Narrow:wght@400&family=Raleway:wght@300&display=swap">
<style>
  :root {
    --blue: #5b8dc0;
    --blue-line: #7ea7cf;
    --logo-blue: #3f6f9f;
    --banner: #e4e8e6;
    --gold: #d4a13a;
    --red: #c81414;
    --text: #333333;
    --heading: #2e2e2e;
    --white: #ffffff;
    --photo-sky: #b9bfcc;
    --photo-city: #5f5a52;
  }
  * { margin: 0; padding: 0; box-sizing: border-box; }
  html, body { width: 1200px; height: 1000px; overflow: hidden; background: var(--white); }
  body { font-family: "PT Sans", Arial, sans-serif; color: var(--text); position: relative; }

  .page { position: absolute; left: 135px; top: 0; width: 911px; height: 1000px; border-left: 1px solid var(--blue-line); border-right: 1px solid var(--blue-line); border-top: 1px solid var(--blue-line); }
  .abs { position: absolute; }

  .top-band { left: 171px; top: 3px; width: 832px; height: 17px; background: var(--blue); }
  .top-rule { left: 171px; top: 21px; width: 832px; height: 1px; background: var(--blue); }

  .main-nav { left: 135px; top: 38px; width: 911px; display: flex; justify-content: center; gap: 12px; font-family: "PT Sans Narrow", Arial, sans-serif; font-size: 20px; color: var(--heading); }
  .main-nav a { color: inherit; text-decoration: none; display: flex; align-items: center; gap: 7px; }

  .bullet { width: 9px; height: 11px; flex: none; }

  .hero-photo { left: 135px; top: 78px; width: 274px; height: 335px; background: linear-gradient(180deg, var(--photo-sky) 0%, #a9b0c0 60%, var(--photo-city) 82%, #4a4338 100%); }
  .hero-band { left: 409px; top: 78px; width: 636px; height: 262px; background: var(--banner); }
  .brand { left: 409px; top: 186px; width: 636px; text-align: center; font-family: "Raleway", Arial, sans-serif; font-weight: 300; font-size: 16px; letter-spacing: 3px; color: var(--logo-blue); text-transform: lowercase; }
  .hero-rule { left: 171px; top: 418px; width: 422px; height: 2px; background: var(--blue-line); }

  .col-divider { left: 414px; top: 452px; width: 1px; height: 548px; background: var(--blue-line); }
  .row-rule { left: 432px; top: 724px; width: 571px; height: 2px; background: var(--blue-line); }
  .sub-divider { left: 764px; top: 757px; width: 1px; height: 243px; background: var(--blue-line); }

  .section-title { display: flex; align-items: center; gap: 8px; font-family: "PT Sans Narrow", Arial, sans-serif; font-weight: 400; font-size: 20px; color: var(--heading); line-height: 1.2; }

  .copy { font-size: 12.5px; line-height: 20px; color: var(--text); }
  .copy a { color: var(--red); text-decoration: underline; white-space: nowrap; }
  .news-date { color: var(--red); font-size: 15px; line-height: 20px; }
  .news-item { margin-bottom: 20px; }
  .lead-blue { color: var(--blue); font-weight: 700; font-size: 13px; line-height: 20px; }
  .lead-gold { color: var(--gold); font-weight: 700; font-size: 13px; line-height: 20px; }

  .thumb { border: 1px solid var(--blue-line); padding: 3px; background: var(--white); }
  .thumb span { display: block; width: 100%; height: 100%; }
</style>
</head>
<body>
  <div class="page"></div>

  <div class="abs top-band"></div>
  <div class="abs top-rule"></div>

  <nav class="abs main-nav">
    <a href="#"><svg class="bullet" viewBox="0 0 9 11"><polygon points="4.5,0 9,2.5 9,8.5 4.5,11 0,8.5 0,2.5" fill="#d9a93c"/><polygon points="4.5,5.5 9,2.5 9,8.5 4.5,11" fill="#9c7420"/></svg>home</a>
    <a href="#"><svg class="bullet" viewBox="0 0 9 11"><polygon points="4.5,0 9,2.5 9,8.5 4.5,11 0,8.5 0,2.5" fill="#d9a93c"/><polygon points="4.5,5.5 9,2.5 9,8.5 4.5,11" fill="#9c7420"/></svg>about us</a>
    <a href="#"><svg class="bullet" viewBox="0 0 9 11"><polygon points="4.5,0 9,2.5 9,8.5 4.5,11 0,8.5 0,2.5" fill="#d9a93c"/><polygon points="4.5,5.5 9,2.5 9,8.5 4.5,11" fill="#9c7420"/></svg>services</a>
    <a href="#"><svg class="bullet" viewBox="0 0 9 11"><polygon points="4.5,0 9,2.5 9,8.5 4.5,11 0,8.5 0,2.5" fill="#d9a93c"/><polygon points="4.5,5.5 9,2.5 9,8.5 4.5,11" fill="#9c7420"/></svg>contact</a>
  </nav>

  <div class="abs hero-photo" role="img" aria-label="Madrid skyline with four business towers above the city"></div>
  <div class="abs hero-band"></div>
  <div class="abs brand">torvelo management</div>
  <div class="abs hero-rule"></div>

  <div class="abs col-divider"></div>
  <div class="abs row-rule"></div>
  <div class="abs sub-divider"></div>

  <section class="abs" style="left:200px; top:474px; width:190px;">
    <h2 class="section-title"><svg class="bullet" viewBox="0 0 9 11"><polygon points="4.5,0 9,2.5 9,8.5 4.5,11 0,8.5 0,2.5" fill="#d9a93c"/><polygon points="4.5,5.5 9,2.5 9,8.5 4.5,11" fill="#9c7420"/></svg>latest news</h2>
    <div style="margin-top:34px;">
      <div class="news-item copy"><div class="news-date">18/10/2005</div>Erat, sed diam voluptua. At vero dolores et ea rebum. sadi pscing elitr, sed dam <a href="#">read more</a></div>
      <div class="news-item copy"><div class="news-date">15/10/2005</div>Erat, sed diam voluptua. At vero dolores et ea rebum. sadi pscing elitr, sed dam <a href="#">read more</a></div>
      <div class="news-item copy"><div class="news-date">14/10/2005</div>Erat, sed diam voluptua. At vero dolores et ea rebum. sadi pscing elitr, sed dam <a href="#">read more</a></div>
    </div>
  </section>

  <section class="abs" style="left:200px; top:849px; width:190px;">
    <h2 class="section-title"><svg class="bullet" viewBox="0 0 9 11"><polygon points="4.5,0 9,2.5 9,8.5 4.5,11 0,8.5 0,2.5" fill="#d9a93c"/><polygon points="4.5,5.5 9,2.5 9,8.5 4.5,11" fill="#9c7420"/></svg>careers</h2>
    <div class="copy" style="margin-top:22px;"><div class="lead-blue">Lorem ipsum dolor sit amet, consetetur sadi pscing sed</div>Erat, sed diam voluptua. At vero eos et accusam et justo duo dolores et ea rebum. Lorem ipsum dolor sit amet</div>
  </section>

  <div class="abs thumb" style="left:432px; top:488px; width:135px; height:192px;"><span role="img" aria-label="Business team working together at a laptop" style="background:linear-gradient(160deg,#3a3330 0%,#8a6a4a 55%,#c9c4bd 100%);"></span></div>
  <div class="abs copy" style="left:593px; top:545px; width:380px;"><div class="lead-blue">Lorem ipsum dolor sit amet, consetetur sadi pscing sed diam</div>Erat, sed diam voluptua. At vero eos et accusam et justo duo dolores et ea rebum. Lorem ipsum dolor sit amet, consetetur sadi pscing elitr, sed dam At vero eos et accusam et justo duo dolores et ea rebum. Lorem ipsum dolor sit amet, consetetur sadi pscing elitr, sed dam <a href="#">read more</a></div>

  <div class="abs thumb" style="left:435px; top:743px; width:101px; height:144px;"><span role="img" aria-label="Hands joined together in teamwork" style="background:linear-gradient(150deg,#f2f2f4 0%,#c99a7c 55%,#2d2b2d 100%);"></span></div>
  <h2 class="abs section-title" style="left:555px; top:746px;"><svg class="bullet" viewBox="0 0 9 11"><polygon points="4.5,0 9,2.5 9,8.5 4.5,11 0,8.5 0,2.5" fill="#d9a93c"/><polygon points="4.5,5.5 9,2.5 9,8.5 4.5,11" fill="#9c7420"/></svg>partners</h2>
  <div class="abs copy" style="left:558px; top:786px; width:195px;"><div class="lead-gold">Lorem ipsum dolor sit amet,</div>dolores et ea rebum. Lorem ipsum dolor sit amet, consetetur sadi pscing elitr, sed dam <a href="#">read more</a></div>

  <div class="abs thumb" style="left:435px; top:903px; width:101px; height:120px;"><span role="img" aria-label="Hand signing a document with a pen" style="background:linear-gradient(150deg,#9a7a52 0%,#d8cbb4 60%,#eeeae2 100%);"></span></div>
  <h2 class="abs section-title" style="left:555px; top:907px;"><svg class="bullet" viewBox="0 0 9 11"><polygon points="4.5,0 9,2.5 9,8.5 4.5,11 0,8.5 0,2.5" fill="#d9a93c"/><polygon points="4.5,5.5 9,2.5 9,8.5 4.5,11" fill="#9c7420"/></svg>clients</h2>
  <div class="abs copy" style="left:558px; top:946px; width:195px;"><div class="lead-gold">Lorem ipsum dolor sit amet,</div>dolores et ea rebum. Lorem ipsum dolor sit amet, consetetur sadi</div>

  <div class="abs thumb" style="left:775px; top:757px; width:93px; height:132px;"><span role="img" aria-label="Customer support agent wearing a headset" style="background:linear-gradient(180deg,#e8e6e4 0%,#b58a6c 50%,#2a2426 100%);"></span></div>
  <h2 class="abs section-title" style="left:880px; top:840px; align-items:flex-start;"><svg class="bullet" viewBox="0 0 9 11" style="margin-top:8px;"><polygon points="4.5,0 9,2.5 9,8.5 4.5,11 0,8.5 0,2.5" fill="#d9a93c"/><polygon points="4.5,5.5 9,2.5 9,8.5 4.5,11" fill="#9c7420"/></svg><span>customer<br>support</span></h2>
  <div class="abs copy" style="left:792px; top:911px; width:195px;"><div class="lead-blue">Lorem ipsum dolor sit amet, consetetur sadi pscing sed</div>eos et accusam et justo duo dolores et ea rebum. Lorem ipsum dolor sit amet, consetetur sadi pscing elitr</div>
</body>
</html>
```